Vantor Drift Shiners packaging design

We need a packaging design for Calder Trailworks LLC. The Brand Name is Vantor Drift Shiners, this is a fishing lure that was developed by a Inland Angling Honor Roll Hall inductee. We would like to see the designs that use the color green in the packaging. the final design should represent quality. excitement and Innovation. The Package size is 3 inches wide and 4 inches tall, this will be a pegged package so the front of the package is all that will need to be designed.
Target Market(s)
age 25-55 Male and Female
Logo Text
Tough and represents quality
Font styles to use
Requirements
Must have
- Vantor Drift Shiners as logo
- Tagline Inspired a Trophy Water Angling Title
- Notes not what to say but have it represented in the design: Bold and strength contemporary and sharp
Nice to have
- na
Should not have
- na

```html
<!DOCTYPE html>
<html lang="en">
<head>
<meta charset="utf-8">
<title>Vantor Drift Shiners – Pegged Package Front</title>
<link rel="stylesheet" href="https://fonts.googleapis.com/css2?family=Arimo:wght@700&family=Open+Sans:wght@700;800&display=swap">
<style>
  :root {
    --pack-green: #00a651;
    --pack-white: #ffffff;
    --swoosh-pale: #a9d18e;
    --band-dark: #0b2a17;
    --band-mid: #5e9a6a;
    --water-light: #6cc0ea;
    --water-deep: #3d4a9c;
  }
  html, body {
    margin: 0;
    padding: 0;
    overflow: hidden;
    background: var(--pack-white);
  }
  .package {
    position: relative;
    width: 900px;
    height: 1200px;
    background: var(--pack-green);
    overflow: hidden;
  }
  .package__art {
    position: absolute;
    inset: 0;
  }
  .maker-name {
    position: absolute;
    top: 222px;
    left: 0;
    width: 900px;
    margin: 0;
    text-align: center;
    font-family: "Arimo", Arial, sans-serif;
    font-weight: 700;
    font-size: 46px;
    line-height: 60px;
    color: var(--pack-white);
  }
  .tagline {
    position: absolute;
    top: 312px;
    left: 0;
    width: 900px;
    margin: 0;
    text-align: center;
    font-family: "Open Sans", Arial, sans-serif;
    font-weight: 800;
    font-size: 66px;
    line-height: 84px;
    letter-spacing: -1.5px;
    color: var(--pack-white);
  }
  .brand-name {
    position: absolute;
    top: 432px;
    left: 170px;
    width: 582px;
    margin: 0;
    text-align: center;
    font-family: "Open Sans", Arial, sans-serif;
    font-weight: 800;
    font-size: 50px;
    line-height: 56px;
    color: var(--pack-white);
  }
</style>
</head>
<body>
  <main class="package">
    <svg class="package__art" width="900" height="1200" viewBox="0 0 900 1200" aria-hidden="true">
      <defs>
        <radialGradient id="swoosh-glow" cx="0.1" cy="0.55" r="0.75">
          <stop offset="0" stop-color="#ffffff"/>
          <stop offset="0.45" stop-color="#ffffff"/>
          <stop offset="1" stop-color="#a9d18e"/>
        </radialGradient>
        <linearGradient id="dark-band" x1="0" y1="1" x2="0.3" y2="0">
          <stop offset="0" stop-color="#0b2a17"/>
          <stop offset="0.5" stop-color="#5e9a6a"/>
          <stop offset="1" stop-color="#0b2a17"/>
        </linearGradient>
        <radialGradient id="water" cx="0.55" cy="0.6" r="0.6">
          <stop offset="0" stop-color="#6cc0ea"/>
          <stop offset="0.6" stop-color="#6cc0ea"/>
          <stop offset="1" stop-color="#3d4a9c"/>
        </radialGradient>
      </defs>

      <path class="peg-hole" fill="#ffffff"
            d="M403,110 V102 Q403,88 417,88 H476 Q490,88 490,102 V110 H537 Q557,110 557,131 Q557,152 537,152 H363 Q343,152 343,131 Q343,110 363,110 Z"/>

      <path class="swoosh-light" fill="url(#swoosh-glow)" stroke="#ffffff" stroke-width="2"
            d="M0,725 C200,900 450,960 760,993 C500,1010 220,1080 0,1170 Z"/>
      <path class="swoosh-dark" fill="url(#dark-band)"
            d="M0,1170 C220,1080 500,1010 760,993 L900,996 C690,1012 400,1080 150,1200 L0,1200 Z"/>
      <path class="swoosh-water" fill="url(#water)"
            d="M150,1200 C400,1080 690,1012 900,996 L900,1200 Z"/>

      <rect class="brand-band" x="170" y="488" width="582" height="40" fill="#ffffff"/>
      <rect class="product-window" x="173" y="546" width="581" height="556" fill="none" stroke="#ffffff" stroke-width="5"/>
    </svg>

    <p class="maker-name">Calder Trailworks LLC</p>
    <p class="tagline">Trophy Water Angling</p>
    <h1 class="brand-name">Vantor Drift Shiners</h1>
  </main>
</body>
</html>
```